Grindstones- Tattoos/Piercings/Motorcycle/Biker Appearl Shop

Grindstones' buisness cards can be creative, playful and eye catching. Incorporate leather or diamond plate. We are an all female business. Biker theme, Tattoo Photos, Piercing Photos, Diamond plate, Leather and Girls!

This project needs to be an appointment card as well for the tattoo artists and piercers. We need a section that says APPT With: _______ , DATE, TIME, and then a QUOTE and DEPOSIT section for the artists. I attached the logo so you could incorportate that and have complete creative freedom. It's a biker store, we sell biker appearl and accessories, with a tattoo and piercing shop connected. Girls, Leather, Tattoos and Piercings. Have fun with it!
Updates

I've Updated project details for better description of what im looking for. Thanks!

Target Market(s)

Male and Female Ages 15-90. Interests in custom tattoos and quality piercings, bikers, motorcycle accessories like helmets, gloves, masks, leather, boots. Jewlery and clothes.

Industry/Entity Type

Business

Contact Information for Business Card

The business is called Grindstones, address, phone number and website. (2847 Larkmoor Rd. Brackwater, OR. 97481 (231)870-4152 www.inkvalleyshop.example)

Font styles to use
Serif
Sans Serif
Decorative
Script

Requirements
Must have
• Appointment with______
• Date_____ or MON TUES WED THUR etc... check mark boxes
• Time_____
• Quote______
• Deposit_______
• (555) 870-4152
• 2847 Larkmoor Rd
• Brackwater, OR 97481
• a facebook logo
Nice to have
• Owner Roy Pemberly
Should not have
• Tribal dragons or anything Tribal.That's cheesy! No Butterflies, No stars. No boys,

```html
<!DOCTYPE html>
<html lang="en">
<head>
<meta charset="utf-8">
<title>Grindstones – Appointment Card</title>
<link href="https://fonts.googleapis.com/css2?family=Josefin+Sans:wght@300;400&family=Allura&display=swap" rel="stylesheet">
<style>
  :root {
    --stage: #dcd9d5;
    --card-front: #f6f7f7;
    --card-band: #eceff0;
    --card-back: #e4eaed;
    --ink-dark: #2b2d30;
    --ink-blue: #4a7fc9;
    --rule-grey: #b9bec3;
    --wing-light: #9dbccb;
    --logo-slate: #4e5d68;
  }
  * { box-sizing: border-box; margin: 0; padding: 0; }
  html, body { width: 1200px; height: 1000px; overflow: hidden; }
  body {
    background: var(--stage);
    font-family: "Josefin Sans", "Helvetica Neue", Arial, sans-serif;
    position: relative;
  }
  .card {
    position: absolute;
    top: 350px;
    width: 520px;
    height: 300px;
    border-radius: 4px;
    box-shadow: 0 6px 18px rgba(0,0,0,0.18);
    overflow: hidden;
  }
  .card--front { left: 60px; background: var(--card-front); }
  .card--back  { left: 620px; background: var(--card-back); }

  .front__band {
    position: absolute; left: 150px; top: 0; width: 230px; height: 100%;
    background: var(--card-band);
  }
  .wing { position: absolute; width: 120px; height: 95px; }
  .wing--left  { left: 22px; top: 42px; }
  .wing--right { right: 22px; bottom: 28px; }

  .website { position: absolute; left: 22px; top: 16px; font-size: 12px; font-weight: 300; color: var(--ink-blue); }
  .phone   { position: absolute; right: 22px; top: 16px; font-size: 14px; font-weight: 300; color: var(--ink-blue); letter-spacing: 0.5px; }

  .owner {
    position: absolute; left: 160px; top: 44px;
    font-family: "Allura", cursive; font-size: 34px; color: var(--ink-dark);
    white-space: nowrap;
  }
  .address {
    position: absolute; left: 170px; top: 94px;
    font-size: 15px; font-weight: 300; line-height: 20px; color: var(--ink-blue);
  }
  .appt {
    position: absolute; left: 170px; top: 146px;
    font-size: 14px; font-weight: 400; color: var(--ink-dark);
  }
  .fields { position: absolute; left: 22px; top: 180px; width: 330px; list-style: none; }
  .field {
    display: flex; align-items: flex-end; height: 26px;
    font-size: 13px; font-weight: 300; color: var(--ink-blue);
  }
  .field__label { width: 64px; }
  .field__line { flex: 1; border-bottom: 1px solid var(--rule-grey); margin-bottom: 3px; }

  .brand {
    position: absolute; inset: 0;
    display: flex; align-items: center; justify-content: center;
    font-size: 74px; font-weight: 400; color: var(--logo-slate); letter-spacing: 1px;
  }
</style>
</head>
<body>
  <section class="card card--front" aria-label="Appointment card front">
    <div class="front__band"></div>
    <svg class="wing wing--left" role="img" aria-label="Blue ornamental wing illustration" viewBox="0 0 120 95">
      <rect width="120" height="95" rx="10" fill="var(--wing-light)"/>
    </svg>
    <svg class="wing wing--right" role="img" aria-label="Blue ornamental wing illustration" viewBox="0 0 120 95">
      <rect width="120" height="95" rx="10" fill="var(--wing-light)"/>
    </svg>

    <p class="website">www.inkvalleyshop.example</p>
    <p class="phone">(555) 870-4152</p>
    <p class="owner">Owner Roy Pemberly</p>
    <p class="address">2847 Larkmoor Rd<br>Brackwater, OR 97481</p>
    <p class="appt">Appointment with</p>

    <ul class="fields">
      <li class="field"><span class="field__label">Date</span><span class="field__line"></span></li>
      <li class="field"><span class="field__label">Time</span><span class="field__line"></span></li>
      <li class="field"><span class="field__label">Quote</span><span class="field__line"></span></li>
      <li class="field"><span class="field__label">Deposit</span><span class="field__line"></span></li>
    </ul>
  </section>

  <section class="card card--back" aria-label="Card back">
    <p class="brand">Grindstones</p>
  </section>
</body>
</html>
```